パック詰めしたカニ身を入れる袋のデザインを依頼させていただきます。中の商品が見えるように、また通販のお客様だけでなく、デパートの食品売り場や高級スーパーで手にとっていただけるような、高級感のあるデザイン案をお願いします。イメージは『和モダン』です。
▼デザインの仕様▼
【袋サイズ】W200×H300(mm)
【デザインしていただく部分】W200×H270(mm)
※袋下30mmは空けておいてください。
商品が入った状態の参考画像は添付ファイル①を参照
(今回は袋のデザインをお願いします)
【色の数】4色まで
【材質】PP

▼記載内容▼※文字サイズ、字体、配置はおまかせいたします。
【商品名】右記よりどれか(かに身 ・ カニ身 ・ 蟹身)
【会社名】北岡商店
【賞味期限印刷用スペース】W30×H10(mm)※白抜きで
【商品特長】以下よりいくつか選択の上記載してください。
※表現は自由に変更してください。
・茹でへのこだわり(アルカリ水、瀬波の白粒使用)
・兵庫 香住港産
・日本海の深層水で育まれた
・みずみずしい
・カニ本来の甘み
【イメージ画像】添付ファイル②参照
※こちらは使っていただいてもいただかなくてもどちらでも結構です。
赤系、グレー系、黒・ゴールド等、高級感のある色
• 高解像度JPG (.jpg)
• イラストレーター形式 (.ai)
参考画像追記しておきます
多くのご提案ありがとうございます。
ご検討いただいているランサーの皆様に弊社よりお願いがあります。

1.依頼開始当初より記載しておりました、『和モダン』というイメージにあまり固執されすぎることなく、各ランサー様の自由な発想でデザインしていただきたい。
2.添付ファイル②のカニの画像は使用しないでください。

大変申し訳ございませんが、既にご提案いただいております皆様も、上記の点を踏まえまして、再度のご検討、ご提案いただければと思います。
残り日数少ない中、急な変更ではございますが何卒宜しくお願い致します。
上記変更に伴い、締め切りを1日延長させていただきます。
よろしくお願いいたします

ご質問等ございましたら、お気軽にお問い合わせ下さい。

・伝えたいことを見ただけで分かりやすくとらえることができる。
・主張しすぎないデザインの中に、高級感、上品さが感じ取れる。
・バランスがよく、中のカニ身を引き立ててくれると感じた。

皆様の貴重なお時間を、弊社依頼に費やしていただきまして、誠にありがとうございました。
今回見送らせていただいた皆様のご提案の中にも、素晴らしいデザインのものが数多くありました。今後もTesmora内におきまして他製品のパッケージやパンフレット等の依頼ができればと思っております。その際は是非また、素敵なご提案をお願いいたします。

```html
<!DOCTYPE html>
<html lang="ja">
<head>
<meta charset="utf-8">
<title>蟹身 パッケージ</title>
<link rel="stylesheet" href="https://fonts.googleapis.com/css2?family=Noto+Serif+JP:wght@500;700;900&display=swap">
<style>
  :root {
    --black: #0d0b08;
    --side-glow: #3a342a;
    --gold-light: #f4dc9a;
    --gold: #c9a24f;
    --gold-dark: #7a5a1c;
    --silver-light: #f2f2f2;
    --silver: #bdbdbd;
    --silver-dark: #8a8a8a;
    --ink: #111111;
    --white: #ffffff;
  }
  html, body {
    margin: 0;
    padding: 0;
    width: 797px;
    height: 1200px;
    overflow: hidden;
    background: var(--white);
  }
  .package {
    position: relative;
    width: 797px;
    height: 1200px;
    font-family: "Noto Serif JP", serif;
  }
  .top-panel {
    position: absolute;
    left: 0; top: 0;
    width: 797px; height: 690px;
  }
  .title-plate {
    position: absolute;
    left: 252px; top: 40px;
    width: 293px; height: 120px;
    background: linear-gradient(180deg, var(--gold-light) 0%, var(--gold) 55%, var(--gold-dark) 100%);
    display: flex; align-items: center; justify-content: center;
    box-shadow: 0 0 0 3px var(--black);
  }
  .product-name {
    margin: 0;
    font-size: 96px;
    font-weight: 900;
    color: var(--black);
    letter-spacing: 6px;
    line-height: 1;
  }
  .lower-panel {
    position: absolute;
    left: 0; top: 680px;
    width: 797px; height: 462px;
    background: linear-gradient(135deg, var(--silver-light) 0%, var(--silver) 35%, var(--silver-light) 55%, var(--silver-dark) 100%);
  }
  .features {
    position: absolute;
    right: 78px; top: 20px;
    height: 360px;
    margin: 0;
    writing-mode: vertical-rl;
    font-size: 27px;
    font-weight: 500;
    line-height: 1.12;
    color: var(--ink);
  }
  .origin {
    position: absolute;
    left: 28px; top: 120px;
    writing-mode: vertical-rl;
    font-size: 27px;
    font-weight: 500;
    color: var(--ink);
    border: 3px solid var(--ink);
    border-radius: 10px;
    padding: 10px 3px;
    line-height: 1.1;
  }
  .shop-name {
    position: absolute;
    left: 266px; top: 397px;
    width: 266px; height: 46px;
    background: linear-gradient(180deg, #3a3a3a, var(--black));
    color: var(--gold-light);
    font-size: 30px;
    font-weight: 700;
    letter-spacing: 8px;
    display: flex; align-items: center; justify-content: center;
    margin: 0;
  }
  .date-space {
    position: absolute;
    left: 612px; top: 410px;
    width: 93px; height: 28px;
    background: var(--white);
  }
</style>
</head>
<body>
<div class="package">
  <svg class="top-panel" width="797" height="690" viewBox="0 0 797 690">
    <defs>
      <linearGradient id="stripe-fade" x1="0" y1="0" x2="1" y2="0">
        <stop offset="0" stop-color="#c9a24f"/>
        <stop offset="0.5" stop-color="#f4dc9a"/>
        <stop offset="1" stop-color="#c9a24f"/>
      </linearGradient>
      <linearGradient id="side-field" x1="0" y1="0" x2="0" y2="1">
        <stop offset="0" stop-color="#3a342a"/>
        <stop offset="0.5" stop-color="#0d0b08"/>
        <stop offset="1" stop-color="#3a342a"/>
      </linearGradient>
      <linearGradient id="crab" x1="0" y1="0" x2="1" y2="1">
        <stop offset="0" stop-color="#e88a6a"/>
        <stop offset="0.5" stop-color="#f6e2cf"/>
        <stop offset="1" stop-color="#d97656"/>
      </linearGradient>
    </defs>
    <rect width="797" height="690" fill="url(#side-field)"/>
    <g class="band-stripes">
      <rect x="110" y="0" width="577" height="690" fill="#0d0b08"/>
      <g fill="url(#stripe-fade)">
        <rect x="110" y="6" width="577" height="7"/><rect x="110" y="22" width="577" height="7"/>
        <rect x="110" y="170" width="577" height="7"/><rect x="110" y="186" width="577" height="7"/>
        <rect x="110" y="202" width="577" height="7"/><rect x="110" y="218" width="577" height="7"/>
        <rect x="110" y="234" width="577" height="7"/><rect x="110" y="250" width="577" height="7"/>
        <rect x="110" y="266" width="577" height="7"/><rect x="110" y="282" width="577" height="7"/>
        <rect x="110" y="298" width="577" height="7"/><rect x="110" y="314" width="577" height="7"/>
        <rect x="110" y="330" width="577" height="7"/><rect x="110" y="346" width="577" height="7"/>
        <rect x="110" y="362" width="577" height="7"/><rect x="110" y="378" width="577" height="7"/>
        <rect x="110" y="394" width="577" height="7"/><rect x="110" y="410" width="577" height="7"/>
        <rect x="110" y="426" width="577" height="7"/><rect x="110" y="442" width="577" height="7"/>
        <rect x="110" y="458" width="577" height="7"/><rect x="110" y="474" width="577" height="7"/>
        <rect x="110" y="490" width="577" height="7"/><rect x="110" y="506" width="577" height="7"/>
        <rect x="110" y="522" width="577" height="7"/><rect x="110" y="538" width="577" height="7"/>
        <rect x="110" y="554" width="577" height="7"/><rect x="110" y="570" width="577" height="7"/>
        <rect x="110" y="586" width="577" height="7"/><rect x="110" y="602" width="577" height="7"/>
        <rect x="110" y="618" width="577" height="7"/><rect x="110" y="634" width="577" height="7"/>
        <rect x="110" y="650" width="577" height="7"/><rect x="110" y="666" width="577" height="7"/>
      </g>
    </g>
    <polygon class="product-window" role="img" aria-label="袋の窓から見えるパック詰めのカニ身"
      points="292,173 505,173 611,405 505,638 292,638 186,405"
      fill="url(#crab)" stroke="#c9a24f" stroke-width="6"/>
  </svg>

  <div class="title-plate"><h1 class="product-name">蟹身</h1></div>

  <section class="lower-panel">
    <p class="features">日本海の深層水で<br>育まれた<br>「みずみずしい蟹」を<br>「アルカリ水」<br>　瀬波の白粒<br>を使用し<br>蟹　本来の甘みを<br>引き出す<br>茹でへのこだわりの<br>美味しさ</p>
    <div class="origin">兵庫 香住港産</div>
    <p class="shop-name">北岡商店</p>
    <div class="date-space" aria-label="賞味期限印刷用スペース"></div>
  </section>
</div>
</body>
</html>
```